Website Velmoraq Athletics

Velmoraq Athletics needs an update for our corporate website www.velmoraqathletics.com.
We feel the current website is too cluttered with various bits and pecies and strive to a more simpler, easier to navigate website.
We encourage designers to start with a blank canvas, but few aspects of the current website should remain:
- The four lines of business: Sports Media Services, Sports Content Services, Sports Event Services and Sports Federation Services should have a central place on the new site.
- The colour scheme of our house style (black, white and grey/silver) needs to be honoured.
- Our logo should remain as it is (with background intact). Focus on our preferred company logo, found here: http://www.velmoraqathletics.com/download/logos/JPEG/VA_logo_on_white.jpg
- A place where visitors can view the latest company headlines. Only the headlines will suffice.
- It should be clear that Velmoraq Athletics is a sports company. An inventive way of linking our ability of providing sports data with sports images would highly appreciated.
All other components of the current website can remain or be removed/tweaked as the designer pleases. We are open to a complete new look and feel.
A redesign of the homepage should have your focus, but it would be great if the frame work of the design is usable for the other pages of our website as well.
Velmoraq Athletics keywords that reflect on our company: fast, accurate, innovative, intelligent, no-nonsense, business-aimed, passionate about sports, global, modern.
Target Market(s)
international media (tv stations, newspapers), sports federations, olympic committees, sports results websites, sport app builders
Look and feel

```html
<!DOCTYPE html>
<html lang="en">
<head>
<meta charset="utf-8">
<title>Velmoraq Athletics</title>
<link href="https://fonts.googleapis.com/css2?family=Open+Sans:wght@300;400;600;700&display=swap" rel="stylesheet">
<style>
:root{
  --bg:#181818;
  --panel:#0f0f0f;
  --panel-edge:#2c2c2c;
  --text:#d6d6d6;
  --muted:#8a8a8a;
  --white:#ffffff;
  --accent:#ff6a00;
  --frame:#5a5a5a;
  --chat:#3b5998;
}
*{box-sizing:border-box;margin:0;padding:0}
html,body{width:984px;height:1200px;overflow:hidden}
body{background:var(--bg);font-family:Arial,Helvetica,sans-serif;color:var(--text);position:relative;font-size:10px}
.abs{position:absolute}
.header{left:0;top:0;width:984px;height:80px;background:linear-gradient(#1c1c1c,#050505);border-bottom:1px solid #333}
.brand{left:100px;top:22px;font-family:'Open Sans',sans-serif;font-weight:700;font-size:22px;color:var(--white);letter-spacing:.5px}
.nav{top:43px;left:418px;display:flex;align-items:center;font-family:'Open Sans',sans-serif;font-size:11.5px;color:var(--white)}
.nav a{color:var(--white);text-decoration:none;padding:0 20px;border-right:1px solid #2a2a2a;line-height:30px}
.nav a:last-child{border:none}
.nav .active{border:2px solid #555;border-radius:16px;background:linear-gradient(#2e2e2e,#111);padding:0 24px;line-height:26px;margin-right:6px}
.follow{top:19px;left:702px;font-weight:700;font-size:9.5px;color:#ccc;display:flex;align-items:center;gap:4px}
.follow i{display:inline-block;width:22px;height:22px;border-radius:4px;margin-left:2px}
.slider{left:103px;top:92px;width:480px;height:305px;background:linear-gradient(#e6e6e6,#6a6a6a 60%,#4a4a4a);border-radius:22px}
.photo{left:14px;top:6px;width:454px;height:268px;border-radius:18px;overflow:hidden;background:linear-gradient(135deg,#3a1a1a,#7a2a2a 25%,#2f6a2f 55%,#1d4a1d);}
.caption{left:0;bottom:0;width:100%;height:56px;background:rgba(0,0,0,.7);padding:10px 12px;font-size:9.5px;line-height:14px;color:#eee;letter-spacing:.3px}
.caption .more{position:absolute;right:24px;bottom:10px;font-size:9px}
.arrow{width:32px;height:32px;border-radius:50%;background:rgba(0,0,0,.5);border:2px solid #999;top:126px}
.dots{left:0;top:282px;width:100%;display:flex;justify-content:center;gap:5px}
.dots i{width:12px;height:12px;border-radius:50%;background:#eee;border:1px solid #888}
.dots i:first-child{background:#555;border-color:#ddd}
.events-title{left:598px;top:101px;font-family:'Open Sans',sans-serif;font-size:17px;color:#ddd}
.events-title span{color:#666}
.events{left:593px;top:127px;width:287px;height:271px;background:linear-gradient(#202020,#050505);border:1px solid #2a2a2a}
.event{position:absolute;left:9px;width:266px}
.event h3{font-family:'Open Sans',sans-serif;font-weight:700;font-size:16px;color:var(--white);letter-spacing:.6px}
.event h3 span{color:var(--accent)}
.count{display:flex;gap:4px;margin-top:6px}
.count b{font-family:Georgia,serif;font-style:italic;font-weight:400;font-size:15px;color:#aaa;border:1px solid #333;padding:3px 5px;height:25px;white-space:nowrap}
.event.sep{border-bottom:1px solid #2a2a2a;padding-bottom:14px}
.card{top:416px;width:186px;height:227px;background:var(--panel);border:1px solid var(--panel-edge)}
.card h2{font-family:'Open Sans',sans-serif;font-weight:400;font-size:15.5px;color:#e8e8e8;padding:6px 0 0 7px;white-space:nowrap;letter-spacing:-.2px}
.card h2.tight{font-size:14.6px;letter-spacing:-.4px;padding-left:5px}
.card h2 span{color:var(--accent)}
.card .art{position:absolute;left:8px;top:36px;width:169px;height:70px;border:1px solid #777}
.card .rule{position:absolute;left:8px;right:8px;top:105px;border-top:1px solid #333}
.card p{position:absolute;left:10px;right:10px;top:132px;font-size:9.5px;line-height:14px;letter-spacing:.4px;color:#ccc}
.card .more{position:absolute;right:14px;top:164px;font-size:9.5px;color:#ccc;letter-spacing:.4px}
.card .tags{position:absolute;left:8px;right:8px;top:188px;font-size:8.5px;color:#888;letter-spacing:.4px;line-height:12px}
.divider{left:108px;top:665px;width:772px;border-top:1px solid #3a3a3a}
.news-badge{left:110px;top:675px;width:48px;height:40px}
.news-title{left:168px;top:686px;font-family:'Open Sans',sans-serif;font-size:16.5px;color:#ddd}
.news-title span,.side h2 span{color:var(--accent)}
.news-item{left:108px;width:470px}
.news-item .thumb{position:absolute;left:0;top:2px;width:50px;height:38px;border:2px solid #fff}
.news-item .body{margin-left:64px;font-size:9.8px;line-height:16px;color:#ddd}
.news-item time{display:block;color:var(--accent);font-weight:700;font-style:italic}
.news-item strong{color:#fff;display:block;white-space:nowrap;font-size:9.6px;letter-spacing:-.1px}
.news-item.sep{border-bottom:1px dashed #2a2a2a;padding-bottom:10px}
.vline{left:612px;top:682px;height:420px;border-left:1px dotted #3a3a3a}
.side{left:627px;width:252px;background:var(--panel);border:1px solid var(--panel-edge)}
.side h2{font-family:'Open Sans',sans-serif;font-weight:400;font-size:16.5px;color:#ddd;position:absolute}
.fame-photo{left:8px;top:37px;width:56px;height:76px;border:2px solid #fff;background:linear-gradient(#3a3a3a,#111)}
.fame-name{left:8px;top:121px;color:var(--accent);font-weight:700;font-size:11px;letter-spacing:.6px}
.fame-info{left:77px;top:40px;width:166px;font-size:8.5px;line-height:12.8px;color:#ddd;text-align:justify}
.fame-more{right:17px;top:123px;font-size:8.5px;color:#ddd}
.quote{left:76px;top:50px;width:168px;font-size:8.5px;line-height:12.8px;color:#eee;text-align:justify}
.quote-by{right:11px;top:118px;font-size:9.5px;color:#fff}
.quote-logo{left:10px;top:54px;width:54px;height:44px;background:#fff;display:flex;align-items:center;justify-content:center;font-weight:700;font-size:8px;color:#c00}
.social{left:627px;top:987px;width:253px;height:137px;background:#fff;border:3px solid #fff;outline:1px solid #555;color:#333}
.social .bar{height:22px;background:var(--chat);color:#fff;font-size:8px;padding:0 8px;display:flex;justify-content:space-between;align-items:center}
.social .bar b{font-size:9px}
.social .page{display:flex;gap:8px;padding:6px 8px;border-bottom:1px solid #ddd;height:44px}
.social .page i{width:28px;height:28px;background:#444}
.social .page b{color:var(--chat);font-size:9px;display:block}
.social .like{display:inline-block;margin-top:4px;border:1px solid #bbb;font-size:7.5px;padding:1px 4px;background:#eee;color:var(--chat)}
.social .fans{padding:3px 8px;font-size:7.5px}
.social .faces{display:flex;gap:4px;padding:0 8px}
.social .faces span{display:block;width:32px;text-align:center;font-size:5px;color:var(--chat)}
.social .faces span i{display:block;width:32px;height:32px;background:linear-gradient(#c9a98a,#6a5a4a);margin-bottom:1px}
.social .foot{padding:2px 8px;font-size:5.5px;color:var(--chat)}
.footer-line{left:0;top:1130px;width:984px;border-top:1px solid #2e2e2e}
.footer-links{left:103px;top:1146px;font-size:9px;color:#aaa;letter-spacing:.4px}
.footer-follow{left:710px;top:1139px;font-size:9px;font-weight:700;color:#ccc;display:flex;align-items:center;gap:4px}
.footer-follow i{width:15px;height:15px;background:#777;border-radius:2px;display:inline-block}
.copyright{left:0;width:984px;top:1174px;text-align:center;font-size:8.5px;color:#aaa;letter-spacing:.3px}
</style>
</head>
<body>
<header class="header abs">
  <div class="brand abs">Velmoraq Athletics</div>
  <nav class="nav abs">
    <a class="active">Home</a><a>About Us</a><a>Contact</a><a>Jobs</a><a>Webshops</a>
  </nav>
  <div class="follow abs">Follow Us On:
    <i style="background:#4a6aa8" role="img" aria-label="Social network link"></i>
    <i style="background:#4ab0e0" role="img" aria-label="Social network link"></i>
    <i style="background:#2a7ab0" role="img" aria-label="Social network link"></i>
    <i style="background:#c33" role="img" aria-label="Video channel link"></i>
  </div>
</header>

<section class="slider abs">
  <div class="photo abs" role="img" aria-label="Football match photo: players contesting the ball on a pitch">
    <div class="caption abs">&#9656; Tom Harland one of England's most memorable goals to defeat old enemy Scotland during Cup '96 at Harlow Park.<span class="more">Read details ...</span></div>
  </div>
  <div class="arrow abs" style="left:18px">
    <svg width="28" height="28" viewBox="0 0 28 28"><path d="M17 8 L10 14 L17 20" stroke="#ddd" stroke-width="2.5" fill="none"/></svg>
  </div>
  <div class="arrow abs" style="left:445px">
    <svg width="28" height="28" viewBox="0 0 28 28"><path d="M11 8 L18 14 L11 20" stroke="#ddd" stroke-width="2.5" fill="none"/></svg>
  </div>
  <div class="dots abs"><i></i><i></i><i></i><i></i><i></i></div>
</section>

<div class="events-title abs">Events We Are <span>Involved In Start In:</span></div>
<section class="events abs">
  <div class="event sep" style="top:12px"><h3><span>Scrum World</span> Cup</h3>
    <div class="count"><b>24 days</b><b>07 hrs</b><b>49 mins</b><b>23 secs</b></div></div>
  <div class="event sep" style="top:95px"><h3><span>Pan-Continental</span> Games</h3>
    <div class="count"><b>24 days</b><b>07 hrs</b><b>49 mins</b><b>23 secs</b></div></div>
  <div class="event" style="top:180px"><h3><span>Summit</span> Games</h3>
    <div class="count"><b>24 days</b><b>07 hrs</b><b>49 mins</b><b>23 secs</b></div></div>
</section>

<article class="card abs" style="left:110px">
  <h2>Sports Media <span>Services</span></h2>
  <div class="art" style="background:linear-gradient(135deg,#0a3a9a,#3a8ae0 60%,#1a4ab0)" role="img" aria-label="Blue sports media banner"></div>
  <div class="rule"></div>
  <p>Ultimate Sports Intelligence for journalists.</p>
  <span class="more">read more &gt;</span>
  <div class="tags">reporters, editors, journalists, illustrators</div>
</article>
<article class="card abs" style="left:305px">
  <h2>Sports Content <span>Services</span></h2>
  <div class="art" style="background:linear-gradient(90deg,#d8e0d8 0,#b8c8c0 33%,#c03030 34%,#7a1a1a 66%,#3aa02a 67%,#1a6a10)" role="img" aria-label="Athlete silhouettes collage"></div>
  <div class="rule"></div>
  <p>Fastest, richest, reliable sports statistics &amp; news channel.</p>
  <span class="more">read more &gt;</span>
  <div class="tags">content managers online properties, sponsors</div>
</article>
<article class="card abs" style="left:500px">
  <h2>Sports Event <span>Services</span></h2>
  <div class="art" style="background:linear-gradient(90deg,#fff,#f4e8f0 40%,#fff)" role="img" aria-label="Tournament emblems on white"></div>
  <div class="rule"></div>
  <p>The best media support an event organizer can get.</p>
  <span class="more">read more &gt;</span>
  <div class="tags" style="text-align:center">event media managers</div>
</article>
<article class="card abs" style="left:694px">
  <h2 class="tight">Sports Federation <span>Services</span></h2>
  <div class="art" style="background:linear-gradient(#fff,#e8e8e8)" role="img" aria-label="Federation emblems on white"></div>
  <div class="rule"></div>
  <p>One stop shop media solutions for federations.</p>
  <span class="more">read more &gt;</span>
  <div class="tags">federation media managers, NOC/Sport performance managers</div>
</article>

<div class="divider abs"></div>

<svg class="news-badge abs" viewBox="0 0 48 40" role="img" aria-label="News and events tag">
  <path d="M24 2 L14 12 M24 2 L34 12" stroke="#999" stroke-width="1.5" fill="none"/>
  <rect x="2" y="11" width="44" height="27" rx="4" fill="#f29a1a" stroke="#444" stroke-width="2"/>
  <text x="24" y="23" font-size="6.5" font-family="Georgia,serif" font-weight="700" text-anchor="middle" fill="#222">NEWS</text>
  <text x="24" y="31" font-size="6.5" font-family="Georgia,serif" font-weight="700" text-anchor="middle" fill="#222">&amp; EVENTS</text>
</svg>
<div class="news-title abs">Latest News / <span>Updates</span></div>

<div class="news-item sep abs" style="top:730px">
  <div class="thumb" style="background:#d0157a" role="img" aria-label="Countdown site thumbnail"></div>
  <div class="body"><time>28-Jul-2011 &gt;&gt;</time><strong>Velmoraq Athletics launches OneMoreYear.com website</strong>The 27th of July marked an important day in the world of sports with just one year to go to the first day of competition for the Northport Summer Games.</div>
</div>
<div class="news-item sep abs" style="top:815px">
  <div class="thumb" style="background:#c8ccc8" role="img" aria-label="Newspaper page thumbnail"></div>
  <div class="body"><time>22-Jul-2011 &gt;&gt;</time><strong>Live Medal Ledger now published by three major newspapers on three continents</strong>Since the birth of the Live Medal Ledger in 2010 the service has been taken up by three major daily newspapers.</div>
</div>
<div class="news-item sep abs" style="top:897px">
  <div class="thumb" style="background:linear-gradient(#2a5aa0,#6aa0d0)" role="img" aria-label="Swimming venue thumbnail"></div>
  <div class="body"><time>21-Jul-2011</time><strong>Velmoraq Athletics provides event services for 14th AQUARA World Championships</strong>After having delivered event services for the 2010 AQUARA World Short Course Swimming Championships in Dubai,</div>
</div>
<div class="news-item abs" style="top:981px">
  <div class="thumb" style="background:linear-gradient(#5a6a8a,#2a2a3a)" role="img" aria-label="Group photo thumbnail"></div>
  <div class="body"><time>23-June-2011</time><strong>South African music group Kindred Road records music video with help of CSR program</strong>During one of Velmoraq Athletics' visits to South Africa, Velmoraq Athletics encountered a group of very talented individuals eager to claim their stake in the music industry.</div>
</div>

<div class="vline abs"></div>

<section class="side abs" style="top:681px;height:145px">
  <svg class="abs" style="left:9px;top:-3px" width="32" height="32" viewBox="0 0 32 32"><path d="M16 2 L20 12 L30 12 L22 19 L25 30 L16 23 L7 30 L10 19 L2 12 L12 12Z" fill="#f7931e"/></svg>
  <h2 style="left:40px;top:4px">Wall of <span>Fame</span></h2>
  <div class="fame-photo abs" role="img" aria-label="Portrait of featured athlete"></div>
  <div class="fame-name abs">Lin Meiyu</div>
  <div class="fame-info abs">Country Valdoria<br>Date of birth 09-Mar-1981<br>Era 1990s, 2000s<br>List of honours Summit Gold: 10m Platform 1997, 2001, 3m Springboard 2001, 2005; World Championship Gold: 10m Platform 1995, 1999</div>
  <div class="fame-more abs">More athletes...</div>
</section>

<section class="side abs" style="top:837px;height:138px">
  <svg class="abs" style="left:4px;top:-3px" width="40" height="36" viewBox="0 0 40 36"><rect x="2" y="2" width="22" height="16" rx="5" fill="#f7931e"/><rect x="10" y="9" width="26" height="18" rx="5" fill="#3a9ae0"/><path d="M18 27 L16 34 L24 27Z" fill="#3a9ae0"/></svg>
  <h2 style="left:49px;top:4px">Recent <span>Comments</span></h2>
  <div class="quote-logo abs" role="img" aria-label="Broadcaster mark placeholder">NORDKANAL</div>
  <div class="quote abs">"Very, very nice work on the live-match Denmark-Norway tonight. Really cool update!!! Send my respect to your people!!! About the invoice: Just send it to me"</div>
  <div class="quote-by abs">Anders Holm, Nordkanal News</div>
</section>

<section class="social abs">
  <div class="bar"><span>Find us on Chatterbox</span><b>Chatterbox</b></div>
  <div class="page"><i role="img" aria-label="Page avatar"></i><div><b>Velmoraq Athletics</b><span class="like">&#10003; Like</span></div></div>
  <div class="fans">988 people like <b>Velmoraq Athletics</b>.</div>
  <div class="faces">
    <span><i role="img" aria-label="Fan avatar"></i>Ana</span>
    <span><i role="img" aria-label="Fan avatar"></i>Sam</span>
    <span><i role="img" aria-label="Fan avatar"></i>Lena</span>
    <span><i role="img" aria-label="Fan avatar"></i>Rosa</span>
    <span><i role="img" aria-label="Fan avatar"></i>Tim</span>
    <span><i role="img" aria-label="Fan avatar"></i>Rob</span>
  </div>
  <div class="foot">Chatterbox social plugin</div>
</section>

<div class="footer-line abs"></div>
<div class="footer-links abs">Home | &nbsp;About Us &nbsp;| &nbsp;Jobs &nbsp;| &nbsp;Contact &nbsp;| &nbsp;Webshop</div>
<div class="footer-follow abs">Follow Us on : &nbsp;<i></i><i></i><i></i><i></i><i></i></div>
<div class="copyright abs">Copyright &copy; Velmoraqathletics. Privacy Policy &nbsp;| &nbsp;Terms of Use</div>
</body>
</html>
```